Stationary - Based On Previous Design

Basic stationary with a header and footer

Target Market(s)

Friends, Colleagues, More friendly than professional

Industry/Entity Type

legal/personal

Colors
00AB8E
00BBA5
67D7C9
C6EFE9
E9F9F6

Requirements
Must have
• Green & White
Nice to have
• I like the "P" on the business card and was thinking that would be for both P's in "PembaPixo"
Should not have
• other colors

```html
<!DOCTYPE html>
<html lang="en">
<head>
<meta charset="utf-8">
<title>PembaPixo Stationery</title>
<link href="https://fonts.googleapis.com/css2?family=Merriweather:wght@700&family=Outfit:wght@300;400&display=swap" rel="stylesheet">
<style>
  :root{
    --teal:#1fa08a;
    --teal-mid:#67d7c9;
    --teal-light:#c6efe9;
    --paper:#ffffff;
    --backdrop:#e0e0e0;
    --shadow:rgba(0,0,0,.45);
  }
  *{margin:0;padding:0;box-sizing:border-box}
  html,body{width:698px;height:1200px;overflow:hidden;background:var(--backdrop)}
  .canvas{position:relative;width:698px;height:1200px}
  .sheet{position:absolute;background:var(--paper);overflow:hidden;box-shadow:4px 4px 5px var(--shadow)}
  .sheet svg.art{position:absolute;inset:0;width:100%;height:100%}
  .letterhead{left:148px;top:72px;width:388px;height:552px}
  .envelope-front{left:79px;top:731px;width:544px;height:198px}
  .envelope-back{left:79px;top:968px;width:544px;height:122px}
  .brand-name{position:absolute;font-family:'Merriweather',Georgia,serif;font-weight:700;color:var(--paper);letter-spacing:.2px;white-space:nowrap;line-height:1}
  .contact{position:absolute;color:var(--paper);white-space:nowrap}
  .contact .person{font-family:'Merriweather',Georgia,serif;font-weight:700;letter-spacing:.2px}
  .contact .line{display:flex;align-items:center;font-family:'Outfit',sans-serif;font-weight:300}
  .contact .line svg{flex:none}
  .letterhead .header-name{left:20px;top:38px;font-size:21px}
  .letterhead .contact{left:239px;top:23px}
  .letterhead .person{font-size:10.5px;margin-bottom:5px}
  .letterhead .line{font-size:6.8px;gap:3px;margin-bottom:3px}
  .letterhead .footer-name{right:16px;bottom:14px;font-size:9px}
  .envelope-front .header-name{left:28px;top:46px;font-size:29px}
  .envelope-front .contact{left:336px;top:32px}
  .envelope-front .person{font-size:15px;margin-bottom:7px}
  .envelope-front .line{font-size:9.6px;gap:4px;margin-bottom:4px}
  .envelope-back .footer-name{right:24px;bottom:14px;font-size:11px}
</style>
</head>
<body>
<main class="canvas">

  <section class="sheet letterhead" aria-label="Letterhead">
    <svg class="art" viewBox="0 0 815 1160" preserveAspectRatio="none" aria-hidden="true">
      <path fill="var(--teal-light)" d="M0,198 C30,205 80,210 140,205 C250,195 380,145 500,142 C400,150 250,215 140,228 C80,233 30,230 0,228 Z"/>
      <path fill="var(--teal-mid)" d="M340,182 C420,160 460,148 500,146 C600,143 700,172 815,238 V295 C720,215 600,160 500,162 C430,163 380,175 340,182 Z"/>
      <path fill="var(--teal)" d="M0,0 H815 V238 C700,170 600,140 500,142 C380,145 250,195 140,205 C80,210 30,205 0,198 Z"/>
      <path fill="none" stroke="var(--paper)" stroke-width="3" d="M0,198 C30,205 80,210 140,205 C250,195 380,145 500,142 C600,140 700,170 815,238"/>
      <path fill="var(--teal-light)" d="M815,1050 C600,1052 420,1110 300,1140 L240,1150 C400,1146 600,1075 815,1073 Z"/>
      <path fill="var(--teal-mid)" d="M0,1058 C80,1110 170,1135 240,1135 C300,1135 360,1130 420,1118 C330,1140 280,1150 240,1150 C160,1152 80,1135 0,1095 Z"/>
      <path fill="var(--teal)" d="M0,1095 C80,1135 160,1152 240,1150 C400,1146 600,1075 815,1073 V1160 H0 Z"/>
      <path fill="none" stroke="var(--paper)" stroke-width="3" d="M0,1095 C80,1135 160,1152 240,1150 C400,1146 600,1075 815,1073"/>
    </svg>
    <div class="brand-name header-name">PembaPixo</div>
    <div class="contact">
      <div class="person">DANIEL WHITCOMBE</div>
      <div class="line">
        <svg width="7" height="6" viewBox="0 0 14 12" aria-hidden="true"><rect x="1" y="1" width="12" height="10" fill="none" stroke="#fff" stroke-width="1.4"/><path d="M1,1 L7,6 L13,1" fill="none" stroke="#fff" stroke-width="1.4"/></svg>
        <span>dwhitcombe@whitcombelaw.com</span>
      </div>
      <div class="line">
        <svg width="6" height="7" viewBox="0 0 12 14" aria-hidden="true"><path d="M6,13 C2,8 1.5,6.5 1.5,5 A4.5,4.5 0 0 1 10.5,5 C10.5,6.5 10,8 6,13 Z" fill="none" stroke="#fff" stroke-width="1.4"/><circle cx="6" cy="5" r="1.6" fill="none" stroke="#fff" stroke-width="1.2"/></svg>
        <span>418 N Larkin Ave Fairview, IL 60999</span>
      </div>
    </div>
    <div class="brand-name footer-name">PembaPixo</div>
  </section>

  <section class="sheet envelope-front" aria-label="Envelope front">
    <svg class="art" viewBox="0 0 1142 415" preserveAspectRatio="none" aria-hidden="true">
      <path fill="var(--teal-light)" d="M0,280 C100,300 250,290 400,255 C550,220 650,200 750,200 C600,205 500,240 400,270 C250,315 100,330 0,320 Z"/>
      <path fill="var(--teal-mid)" d="M560,222 C660,205 720,199 780,199 C930,200 1050,270 1142,335 V415 C1050,340 950,245 820,232 C740,226 650,226 560,222 Z"/>
      <path fill="var(--teal)" d="M0,0 H1142 V335 C1050,270 930,200 780,199 C600,196 480,240 400,258 C250,292 100,298 0,278 Z"/>
      <path fill="none" stroke="var(--paper)" stroke-width="4" d="M0,278 C100,298 250,292 400,258 C480,240 600,196 780,199 C930,200 1050,270 1142,335"/>
    </svg>
    <div class="brand-name header-name">PembaPixo</div>
    <div class="contact">
      <div class="person">DANIEL WHITCOMBE</div>
      <div class="line">
        <svg width="10" height="9" viewBox="0 0 14 12" aria-hidden="true"><rect x="1" y="1" width="12" height="10" fill="none" stroke="#fff" stroke-width="1.3"/><path d="M1,1 L7,6 L13,1" fill="none" stroke="#fff" stroke-width="1.3"/></svg>
        <span>dwhitcombe@whitcombelaw.com</span>
      </div>
      <div class="line">
        <svg width="9" height="10" viewBox="0 0 12 14" aria-hidden="true"><path d="M6,13 C2,8 1.5,6.5 1.5,5 A4.5,4.5 0 0 1 10.5,5 C10.5,6.5 10,8 6,13 Z" fill="none" stroke="#fff" stroke-width="1.3"/><circle cx="6" cy="5" r="1.6" fill="none" stroke="#fff" stroke-width="1.1"/></svg>
        <span>418 N Larkin Ave Fairview, IL 60999</span>
      </div>
    </div>
  </section>

  <section class="sheet envelope-back" aria-label="Envelope back">
    <svg class="art" viewBox="0 0 1142 257" preserveAspectRatio="none" aria-hidden="true">
      <path fill="var(--teal-light)" d="M1142,103 C950,100 750,150 560,205 C800,140 950,135 1142,137 Z"/>
      <path fill="var(--teal-mid)" d="M0,115 C80,170 180,215 320,225 C400,230 480,225 560,205 C480,235 400,245 320,245 C200,245 100,225 0,162 Z"/>
      <path fill="var(--teal)" d="M0,162 C100,225 200,245 320,245 C550,245 800,130 1142,137 V257 H0 Z"/>
      <path fill="none" stroke="var(--paper)" stroke-width="4" d="M0,162 C100,225 200,245 320,245 C550,245 800,130 1142,137"/>
    </svg>
    <div class="brand-name footer-name">PembaPixo</div>
  </section>

</main>
</body>
</html>
```